Eid Mubarak Digital Graphic

We seek designs for a digital greeting wishing our clients an Eid Mubarak. The graphic can contain Arabic and English text. This digital greeting should include our company logo.

Target Market(s)

Clients both commercial and government

Industry/Entity Type

Consulting

Font styles to use
Serif
Sans Serif
Decorative
Script
Other font styles liked:
• Arabic calligraphy

Requirements
Must have
• Digital graphic in a format easily sent by email and text
Company logo
Traditional Arabic greeting
Original graphic, not copied
Nice to have
• Arabic calligraphy
Should not have
• Nothing offensive to the Islamic religion

```html
<!DOCTYPE html>
<html lang="en">
<head>
<meta charset="utf-8">
<title>Eid Mubarak Greeting</title>
<link rel="stylesheet" href="https://fonts.googleapis.com/css2?family=Amiri:wght@700&family=Great+Vibes&family=Cinzel:wght@400;500&display=swap">
<style>
  :root {
    --gold-dark: #a9832f;
    --gold-mid: #cfa550;
    --gold-light: #ecc875;
    --navy-pattern: #2c3045;
    --navy-deep: #0f1120;
    --navy-glow: #22273d;
  }
  html, body {
    margin: 0;
    padding: 0;
    width: 1200px;
    height: 1200px;
    overflow: hidden;
    background: var(--navy-deep);
  }
  .greeting-card {
    position: relative;
    width: 1200px;
    height: 1200px;
  }
  .card-art {
    position: absolute;
    inset: 0;
  }
  .greeting-text {
    position: absolute;
    left: 0;
    width: 1200px;
    text-align: center;
    margin: 0;
    background: linear-gradient(180deg, var(--gold-light) 0%, var(--gold-mid) 55%, var(--gold-dark) 100%);
    -webkit-background-clip: text;
    background-clip: text;
    color: transparent;
  }
  .greeting-arabic {
    top: 318px;
    font-family: "Amiri", serif;
    font-weight: 700;
    font-size: 118px;
    line-height: 1;
    direction: rtl;
  }
  .greeting-eid {
    top: 468px;
    font-family: "Great Vibes", cursive;
    font-size: 210px;
    line-height: 1;
    padding-right: 10px;
  }
  .greeting-mubarak {
    top: 688px;
    font-family: "Cinzel", serif;
    font-weight: 500;
    font-size: 48px;
    line-height: 1;
    letter-spacing: 0.42em;
    padding-left: 0.42em;
  }
  .company-name {
    position: absolute;
    top: 862px;
    left: 0;
    width: 1200px;
    margin: 0;
    text-align: center;
    font-family: "Cinzel", serif;
    font-weight: 400;
    font-size: 26px;
    line-height: 1;
    letter-spacing: 0.08em;
    color: var(--gold-mid);
  }
</style>
</head>
<body>
<main class="greeting-card">
  <svg class="card-art" width="1200" height="1200" viewBox="0 0 1200 1200">
    <defs>
      <linearGradient id="goldStroke" x1="0" y1="0" x2="1" y2="1">
        <stop offset="0" stop-color="#8c6e2c"/>
        <stop offset="0.5" stop-color="#d6b060"/>
        <stop offset="1" stop-color="#8c6e2c"/>
      </linearGradient>
      <radialGradient id="innerGlow" cx="0.5" cy="0.5" r="0.55">
        <stop offset="0" stop-color="#23283e"/>
        <stop offset="1" stop-color="#0d0f1c"/>
      </radialGradient>
      <path id="archFrame" d="M600,69 C630,105 690,140 760,160 C850,185 879,240 879,326 C975,326 1045,380 1050,464 C1055,530 1075,575 1107,600 C1075,625 1055,670 1050,736 C1045,820 975,874 879,874 C879,960 850,1015 760,1040 C690,1060 630,1095 600,1131 C570,1095 510,1060 440,1040 C350,1015 321,960 321,874 C225,874 155,820 150,736 C145,670 125,625 93,600 C125,575 145,530 150,464 C155,380 225,326 321,326 C321,240 350,185 440,160 C510,140 570,105 600,69 Z"/>
    </defs>

    <rect class="card-border" x="0" y="0" width="1200" height="1200" fill="url(#goldStroke)"/>
    <rect class="card-pattern" x="18" y="18" width="1164" height="1164" fill="var(--navy-pattern)" role="img" aria-label="Raised arabesque scroll pattern in dark slate across the card face"/>

    <use class="arch-outer" href="#archFrame" fill="url(#goldStroke)"/>
    <use class="arch-band" href="#archFrame" fill="#12152a" transform="translate(600 600) scale(0.955) translate(-600 -600)"/>
    <use class="arch-inner-line" href="#archFrame" fill="url(#goldStroke)" transform="translate(600 600) scale(0.905) translate(-600 -600)"/>
    <use class="arch-field" href="#archFrame" fill="url(#innerGlow)" transform="translate(600 600) scale(0.9) translate(-600 -600)"/>
  </svg>

  <p class="greeting-text greeting-arabic" lang="ar">عيد مبارك</p>
  <p class="greeting-text greeting-eid">Eid</p>
  <p class="greeting-text greeting-mubarak">MUBARAK</p>

  <p class="company-name">Meridian Guard Advisory</p>
</main>
</body>
</html>
```